Re-design existing website and add products for sale.

Our current website is very basic and cluttered. (brightwillowcare.com.au)We want a modern looking website that is easy to navigate. We also want to start selling essential oils and crystal products, so there needs to be a separate page for this. Also needs to be easily edited as we need to change the monthly oracle card with the description. Would like calming colours as we are all about natural healing. Alongside the services listed there should be a button to book now which asks for their name, email, phone number ect. and adds it to the cart.

• Logo is still being designed, please leave a space for the logo which will basically be a lotus flower within a mandala.

```html
<!DOCTYPE html>
<html lang="en">
<head>
<meta charset="utf-8">
<title>Bright Willow Care – Services</title>
<link href="https://fonts.googleapis.com/css2?family=Barlow+Semi+Condensed:wght@300;400;500;600&display=swap" rel="stylesheet">
<style>
:root{
  --magenta:#d61aa8;
  --ink:#1d1d1d;
  --text:#3a3a3a;
  --muted:#5a5a5a;
  --panel:#f3ede4;
  --band:#eaf0f3;
  --band-grey:#eeeeee;
  --line:#c9c9c9;
  --footer:#4a4a4a;
  --footer-text:#f2f2f2;
  --sky:#dde9f3;
  --sand:#efe6cf;
  --lilac:#e7c6df;
}
*{box-sizing:border-box;margin:0;padding:0}
html,body{width:706px;height:1200px;overflow:hidden}
body{font-family:"Barlow Semi Condensed",Arial,sans-serif;color:var(--text);
  background:linear-gradient(180deg,var(--sky) 0%,#e6e8e4 18%,var(--sand) 45%,#e4e8e6 65%,var(--sky) 85%);
  position:relative}
.abs{position:absolute}
/* nav */
.nav{top:0;left:0;width:706px;height:26px;background:#d7e3ec;border-bottom:1px solid #c5d3de}
.nav .social{left:133px;top:8px;display:flex;gap:6px}
.dot{width:9px;height:9px;border-radius:50%;background:var(--ink)}
.dot.active{background:var(--magenta)}
.nav ul{list-style:none;position:absolute;left:306px;top:0;display:flex;gap:0}
.nav li{font-size:7.5px;font-weight:600;letter-spacing:.2px;color:var(--ink);height:25px;line-height:25px;padding:0 8px}
.nav li.home{color:#888}
.nav li.current{color:var(--magenta);border-bottom:1.5px solid var(--magenta)}
.nav li.cart{display:flex;align-items:center;gap:3px}
/* hero */
.brand{left:154px;top:96px;font-size:19px;font-weight:500;color:var(--magenta);letter-spacing:.2px}
.tagline{left:154px;top:120px;font-size:12.5px;font-weight:400;color:var(--ink);line-height:1.3;width:200px}
.feature{left:154px;display:flex;align-items:center;gap:30px;font-size:8px;color:var(--ink);line-height:1.4}
.feature .icon{width:36px;height:30px}
.lotus-mark{width:34px;height:30px;background:var(--ink);border-radius:50% 50% 40% 40%;opacity:.85}
.intro{left:374px;top:97px;width:178px;font-size:8px;line-height:1.45;color:var(--ink)}
.intro p{padding-bottom:8px;margin-bottom:8px;border-bottom:1px solid var(--lilac)}
.intro p:last-child{border:none}
.deco{background:var(--lilac);opacity:.45}
/* services panel */
.panel{left:132px;top:290px;width:442px;height:176px;background:var(--panel);box-shadow:0 1px 3px rgba(0,0,0,.2)}
.panel h2{font-size:12px;font-weight:400;color:var(--ink);letter-spacing:.2px}
.svc{left:22px;top:20px}
.svc ul{margin:10px 0 0 15px;font-size:7.5px;line-height:11.4px;color:var(--text)}
.divider{left:221px;top:22px;width:1px;height:132px;background:var(--line)}
.book{left:243px;top:20px;width:177px}
.field{height:13px;margin-top:10px;background:#fff;border:1px solid var(--line);border-radius:1px;font-size:5.5px;font-style:italic;color:#999;padding:3px 3px;display:flex;justify-content:space-between}
.field.first{margin-top:8px}
.caret{width:0;height:0;border-left:3px solid transparent;border-right:3px solid transparent;border-top:3px solid var(--magenta);margin-top:2px}
.btn{margin-top:10px;height:15px;background:var(--magenta);color:#fff;font-size:6px;font-weight:600;text-align:center;line-height:15px;border-radius:1px}
/* bands */
.band{box-shadow:0 1px 3px rgba(0,0,0,.25)}
.photo{border:1px solid #999}
.band h3{font-size:13px;font-weight:400;color:var(--ink);letter-spacing:.2px}
.band h3 span{color:var(--magenta)}
.price{font-size:7.5px;font-weight:500;color:var(--ink);line-height:1.35;margin-top:4px}
.copy{font-size:5.6px;line-height:1.42;color:var(--muted)}
.copy b{color:var(--ink)}
.copy p{margin-top:6px}
/* footer */
.footer{left:0;top:1076px;width:706px;height:124px;background:var(--footer);color:var(--footer-text)}
.fnav{left:183px;top:17px;list-style:none;font-size:5.5px;font-weight:600;line-height:11px}
.fnav .current{color:var(--magenta)}
.fsep{top:15px;width:1px;height:86px;background:#6b6b6b}
.contact{left:294px;top:16px;width:118px;font-size:5.5px;font-weight:600}
.contact .in{background:#fff;height:9px;margin-top:4px;font-size:5px;font-style:italic;color:#999;font-weight:400;padding:1px 3px}
.contact .msg{height:42px}
.send{margin:4px 0 0 90px;width:28px;height:8px;border:1px solid #fff;font-size:5px;text-align:center;line-height:7px}
.details{left:468px;top:16px;font-size:5.5px;line-height:11px}
.details .social{display:flex;gap:6px;margin-top:3px}
.details .dot{background:#fff;width:8px;height:8px}
.details .dot.active{background:var(--magenta)}
</style>
</head>
<body>

<header class="abs nav">
  <div class="abs social"><span class="dot active" role="img" aria-label="Social link"></span><span class="dot" role="img" aria-label="Social link"></span></div>
  <ul>
    <li class="home">HOME</li><li>PRODUCTS</li><li class="current">SERVICES</li><li>ABOUT</li><li>CONTACT</li>
    <li class="cart"><svg width="11" height="9" viewBox="0 0 11 9"><path d="M0 1h2l1.5 5h6l1.2-4H3" fill="none" stroke="#1d1d1d" stroke-width="1.2"/><circle cx="4" cy="8" r=".9" fill="#1d1d1d"/><circle cx="8.5" cy="8" r=".9" fill="#1d1d1d"/></svg>CART</li>
  </ul>
</header>

<div class="abs deco" role="img" aria-label="Faint lotus flower line decoration" style="left:540px;top:78px;width:110px;height:120px;border-radius:50% 50% 45% 45%;opacity:.25"></div>
<div class="abs deco" role="img" aria-label="Faint sacred symbol decoration" style="left:614px;top:545px;width:50px;height:70px;border-radius:40%;opacity:.3"></div>
<div class="abs deco" role="img" aria-label="Faint sacred symbol decoration" style="left:42px;top:732px;width:46px;height:70px;border-radius:40%;opacity:.3"></div>
<div class="abs deco" role="img" aria-label="Faint sacred symbol decoration" style="left:550px;top:908px;width:100px;height:100px;border-radius:30%;opacity:.3"></div>

<h1 class="abs brand">BRIGHT WILLOW CARE</h1>
<p class="abs tagline">Find Your True Self and Bring Balance to Your LifeBright Willow Care</p>

<div class="abs feature" style="top:172px">
  <div class="icon"><div class="lotus-mark" role="img" aria-label="Lotus icon"></div></div>
  <span>Learn Reiki or Seichim<br>for yourself</span>
</div>
<div class="abs feature" style="top:222px">
  <svg class="icon" viewBox="0 0 36 30"><path d="M2 6h32v6a3 3 0 0 0 0 6v6H2v-6a3 3 0 0 0 0-6z" fill="none" stroke="#1d1d1d" stroke-width="2.4"/><text x="18" y="20" font-size="12" font-weight="700" text-anchor="middle" fill="#1d1d1d" font-family="Arial,sans-serif">%</text></svg>
  <span>10% of proceeds from all services<br>are donated to a charity</span>
</div>

<div class="abs intro">
  <p>Are you struggling through life, feeling stuck, not feeling yourself, or simply feeling drained? Need to find a way to relax and rejuvenate, a way to free up your energy to work on that which better serves you in this lifetime?</p>
  <p>Working together with you, I can help you achieve this. Whether through spiritual healing sessions using Reiki and Seichim, through Oracle Card Readings or a combination of these.</p>
  <p>I am passionate about using my knowledge and skills to help others struggling through their life journey.</p>
</div>

<section class="abs panel">
  <div class="abs svc">
    <h2>OUR SERVICES</h2>
    <ul>
      <li>Reiki &amp; Seichim Healings</li><li>Energy Healing</li><li>Chakra Balancing</li><li>Energy Balancing</li><li>Past Life Clearing</li><li>Oracle Card Readings/Online Readings</li><li>Distant Healing</li><li>Reiki &amp; Seichim Workshops</li><li>Crystals &amp; Hand Made Jewellery Available</li><li>Essential Oil Roll On Blends Available</li>
    </ul>
  </div>
  <div class="abs divider"></div>
  <div class="abs book">
    <h2>BOOK NOW</h2>
    <div class="field first">*full name</div>
    <div class="field">*e-mail address</div>
    <div class="field">*phone number</div>
    <div class="field">*choose service<span class="caret"></span></div>
    <div class="btn">ADD TO THE CARD</div>
  </div>
</section>

<section class="abs band" style="left:0;top:502px;width:574px;height:155px;background:var(--band)">
  <div class="abs photo" role="img" aria-label="Photo of two cupped hands with light between them" style="left:133px;top:15px;width:146px;height:124px;background:radial-gradient(circle at 50% 50%,#fff 0%,#f3d9c6 35%,#c98d6e 60%,#fff 85%)"></div>
  <div class="abs" style="left:297px;top:12px;width:258px">
    <h3>REIKI &amp; SEICHIM <span>HEALINGS</span></h3>
    <div class="price">1 Hour - $75<br>1/2 Hour - $40</div>
    <div class="copy">
      <p><b>Reiki</b> is a non-intrusive, wonderful hands-on healing technique, which can help boost and balance your energy levels, strengthen your immune system, help you relax and let go of stress and tension and help to maintain your overall health and wellbeing. It can help clear blockages and clear past lives and is a great technique for cleansing the body and breaking down stale energy blockages.</p>
      <p><b>Seichim</b> is an ancient and sacred healing modality. It is an advanced form of healing which involves the use of sacred geometry symbols using two hands.<br>It helps clear past lives in a different way to Reiki and helps release blockages from your energy field. It is a form of healing which has been taught in many mystery schools in ancient times. Seichim is said to be the parent energy of all hands-on healing systems and is believed to have originated from Atlantean times.</p>
    </div>
  </div>
</section>

<section class="abs band" style="left:132px;top:693px;width:574px;height:154px;background:var(--band)">
  <div class="abs" style="left:18px;top:12px;width:260px">
    <h3>REIKI &amp; SEICHIM <span>WORKSHOPS</span></h3>
  </div>
  <div class="abs" style="left:18px;top:31px;width:100px">
    <div class="price" style="margin:0">Reiki 1 Workshop - $180<br>Reiki 2 Workshop - $280<br>Seichim Workshop - $460</div>
    <div class="copy"><p>Have you had the chance to experience Reiki or Seichim and now wish to further your knowledge of these ancient healing techniques and use them to help yourself and others around you?</p><p>Would you like to feel more grounded, self empowered, confident and relaxed?</p></div>
  </div>
  <div class="abs copy" style="left:147px;top:32px;width:125px">
    Reiki is Japanese for Universal Life Force Energy.<br>Rei = Universal<br>Ki = Vital Energy
    <p>I offer Reiki 1 &amp; 2 workshops as well as Seichim workshops where I work one on one with you to teach you these wonderful techniques.</p>
    <p><b>Prerequisites:</b><br>Reiki 1 - None<br>Reiki 2 - Reiki 1 Certificate<br>Isis Seichim - Reiki 1 &amp; 2 Certificates</p>
  </div>
  <div class="abs photo" role="img" aria-label="Photo of open hands beneath glowing chakra lights" style="left:294px;top:15px;width:146px;height:124px;background:linear-gradient(135deg,#7a6fb0,#c8b7d9 45%,#8fc3a8 75%,#5e7ea8)"></div>
</section>

<section class="abs band" style="left:0;top:884px;width:464px;height:155px;background:var(--band-grey)">
  <div class="abs photo" role="img" aria-label="Illustrated oracle card of a figure in a violet hooded robe" style="left:133px;top:15px;width:146px;height:124px;background:linear-gradient(180deg,#b06aa6,#d8a9cf 50%,#8c4f8a)"></div>
  <div class="abs" style="left:297px;top:12px;width:150px">
    <h3>ORACLE <span>CARD READINGS</span></h3>
    <div class="price">20 Min - $30</div>
    <div class="copy"><p>Oracle cards, also known as wisdom cards are cards used for divination, fortune telling and spiritual guidance.</p><p>Oracle cards are the modern version of tarot cards, which have been used for centuries by people to find meaningful answers to questions about their life, spiritual path and future.</p></div>
  </div>
</section>

<footer class="abs footer">
  <ul class="abs fnav"><li>CART</li><li>HOME</li><li class="current">PRODUCTS</li><li>SERVICES</li><li>ABOUT</li><li>CONTACT</li></ul>
  <div class="abs fsep" style="left:266px"></div>
  <div class="abs contact">
    CONTACT ME:
    <div class="in">*Name</div>
    <div class="in">*Email</div>
    <div class="in msg">Message</div>
    <div class="send">SEND</div>
  </div>
  <div class="abs fsep" style="left:440px"></div>
  <div class="abs details">
    Tel: 0400 123 456<br>14 Larch Street<br>Kenwick, SA 5019<br>hello@brightwillowcare.com.au
    <div class="social"><span class="dot" role="img" aria-label="Social link"></span><span class="dot active" role="img" aria-label="Social link"></span></div>
  </div>
</footer>

</body>
</html>
```